FC Blavin - Creation of a AD banner for our yearly event

We are a local soccer club in Switzerland. We're organizing a event that will substitute to our yearly club dinner. We need a banner AD to promote on the social networks this event.
We would like to see design that use one or the 2 colors of the club (blue and red).
This Ad should link to a online shop where we can buy vouchers.

Requirements
Must have
• Logo of the club
Title : Souper de gala quand même
Call to action : Plus d'informations
Side texte : Grande Tombola
Banner size : W300xH250 or W300xH600
Nice to have
• Promotion texte: Soutenez le FC Blavin et les restaurateurs locaux

```html
<!DOCTYPE html>
<html lang="fr">
<head>
<meta charset="utf-8">
<title>FC Blavin – Bannières Souper de Gala</title>
<link rel="stylesheet" href="https://fonts.googleapis.com/css2?family=Open+Sans:wght@400;700;800&family=Roboto+Condensed:wght@700&family=Exo+2:ital,wght@1,900&display=swap">
<style>
  :root {
    --page-bg: #ffffff;
    --label-grey: #9a9a9a;
    --teal-deep: #1a8fb0;
    --teal: #2aa6a8;
    --green: #7cc94a;
    --club-red: #e8243c;
    --club-blue: #1c7fd0;
    --title-blue-top: #2a9ee8;
    --title-blue-bottom: #2456a8;
    --title-red-top: #e0304a;
    --title-red-bottom: #6e3a8a;
    --white: #ffffff;
    --ink: #111111;
  }
  * { box-sizing: border-box; margin: 0; padding: 0; }
  html, body { width: 1200px; height: 1000px; overflow: hidden; background: var(--page-bg); }
  body { position: relative; font-family: "Open Sans", Arial, sans-serif; }

  .size-label {
    position: absolute; top: 40px;
    font: 700 26px/1 "Open Sans", Arial, sans-serif;
    color: var(--label-grey); letter-spacing: 0.5px;
  }
  .size-label--square { left: 62px; }
  .size-label--tall { left: 720px; }

  .banner {
    position: absolute; overflow: hidden;
    background:
      radial-gradient(ellipse at 50% 45%, var(--green) 0%, rgba(124,201,74,0) 55%),
      linear-gradient(135deg, var(--teal-deep) 0%, var(--teal) 45%, var(--teal-deep) 100%);
    box-shadow: 4px 6px 8px rgba(0,0,0,0.35);
  }
  .banner--square { left: 62px; top: 82px; width: 630px; height: 525px; }
  .banner--tall { left: 720px; top: 82px; width: 420px; height: 836px; }

  .banner__facets { position: absolute; inset: 0; width: 100%; height: 100%; }

  .club-mark {
    position: absolute; display: flex; align-items: center; gap: 8px;
    font: 800 26px/1 "Open Sans", Arial, sans-serif; color: var(--white);
  }
  .club-mark__dot { width: 22px; height: 22px; border-radius: 50%; background: var(--club-red); flex: none; }
  .banner--square .club-mark { left: 14px; top: 20px; }
  .banner--tall .club-mark { left: 50%; top: 60px; transform: translateX(-50%); font-size: 30px; }

  .event-title {
    position: absolute; text-align: center;
    font-family: "Roboto Condensed", "Arial Narrow", sans-serif; font-weight: 700;
    line-height: 1; white-space: nowrap;
  }
  .event-title span {
    display: block;
    -webkit-background-clip: text; background-clip: text; color: transparent;
    filter: drop-shadow(2px 0 0 #fff) drop-shadow(-2px 0 0 #fff) drop-shadow(0 2px 0 #fff) drop-shadow(0 -2px 0 #fff) drop-shadow(2px 3px 3px rgba(0,0,0,0.35));
  }
  .event-title__top { background-image: linear-gradient(180deg, var(--title-blue-top), var(--title-blue-bottom)); }
  .event-title__bottom { background-image: linear-gradient(180deg, var(--title-red-top), var(--title-red-bottom)); letter-spacing: -0.5px; }

  .banner--square .event-title { left: 150px; width: 466px; top: 12px; }
  .banner--square .event-title__top { font-size: 70px; }
  .banner--square .event-title__bottom { font-size: 58px; margin-top: 8px; }
  .banner--tall .event-title { left: 10px; width: 400px; top: 200px; }
  .banner--tall .event-title__top { font-size: 62px; }
  .banner--tall .event-title__bottom { font-size: 50px; margin-top: 8px; }

  .support-text {
    position: absolute; color: var(--white); font-weight: 700;
    text-shadow: 1px 2px 3px rgba(0,0,0,0.3);
  }
  .banner--square .support-text { left: 14px; top: 212px; font-size: 39px; line-height: 48px; }
  .banner--tall .support-text { left: 18px; top: 346px; font-size: 34px; line-height: 43px; }

  .player-art {
    position: absolute;
    background: radial-gradient(ellipse at 55% 50%, rgba(232,36,60,0.75) 0%, rgba(30,30,30,0.55) 45%, rgba(28,127,208,0.35) 70%, rgba(28,127,208,0) 78%);
  }
  .banner--square .player-art { left: 450px; top: 165px; width: 185px; height: 300px; }
  .banner--tall .player-art { left: 245px; top: 430px; width: 180px; height: 350px; }

  .raffle {
    position: absolute; font-family: "Exo 2", "Arial Black", sans-serif;
    font-style: italic; font-weight: 900; line-height: 0.95; letter-spacing: 3px;
    color: var(--white); -webkit-text-stroke: 2px var(--ink); paint-order: stroke fill;
    text-shadow: 3px 3px 0 var(--ink);
  }
  .raffle__line { display: block; }
  .raffle__line--indent { padding-left: 26px; }
  .banner--square .raffle { left: 188px; top: 352px; font-size: 52px; }
  .banner--square .raffle__line:last-child { margin-left: -2px; }
  .banner--tall .raffle { left: 18px; top: 652px; font-size: 48px; }

  .info-bar {
    position: absolute; left: 0; right: 0; bottom: 0;
    background: var(--club-red); color: var(--white); text-align: center;
  }
  .info-bar::before {
    content: ""; position: absolute; left: 0; right: 0; bottom: 100%;
    height: 8px; background: var(--club-red);
    clip-path: polygon(0 100%, 20% 0, 80% 0, 100% 100%);
  }
  .info-bar strong { font-weight: 800; letter-spacing: 0.3px; }
  .banner--square .info-bar { height: 28px; font-size: 16px; line-height: 28px; }
  .banner--tall .info-bar { height: 20px; font-size: 12px; line-height: 20px; }
</style>
</head>
<body>

<div class="size-label size-label--square">300 x 250</div>
<div class="size-label size-label--tall">300 x 600</div>

<section class="banner banner--square" aria-label="Bannière 300 x 250">
  <svg class="banner__facets" viewBox="0 0 630 525" preserveAspectRatio="none" aria-hidden="true">
    <polygon points="120,525 330,315 540,525" fill="#ffffff" opacity="0.08"/>
    <polygon points="330,0 480,150 630,0" fill="#ffffff" opacity="0.07"/>
    <polygon points="0,60 180,240 0,420" fill="#ffffff" opacity="0.06"/>
    <polygon points="400,320 630,90 630,525" fill="#9be07a" opacity="0.12"/>
  </svg>
  <div class="club-mark"><span class="club-mark__dot"></span>FC Blavin</div>
  <h1 class="event-title">
    <span class="event-title__top">Souper de</span>
    <span class="event-title__bottom">Gala Quand Même</span>
  </h1>
  <p class="support-text">Soutenez Le FC Blavin<br>et Les Restaurateurs<br>Locaux</p>
  <div class="player-art" role="img" aria-label="Illustration d'un joueur de football en maillot rouge devant un cercle bleu et rouge"></div>
  <p class="raffle"><span class="raffle__line raffle__line--indent">GRANDE</span><span class="raffle__line">TOMBOLA</span></p>
  <p class="info-bar">Plus d'informations : <strong>www.fcblavin.ch</strong></p>
</section>

<section class="banner banner--tall" aria-label="Bannière 300 x 600">
  <svg class="banner__facets" viewBox="0 0 420 836" preserveAspectRatio="none" aria-hidden="true">
    <polygon points="0,420 200,620 0,820" fill="#ffffff" opacity="0.08"/>
    <polygon points="260,0 420,160 420,0" fill="#ffffff" opacity="0.07"/>
    <polygon points="60,836 260,636 420,796 420,836" fill="#9be07a" opacity="0.12"/>
    <polygon points="0,0 150,150 0,300" fill="#ffffff" opacity="0.05"/>
  </svg>
  <div class="club-mark"><span class="club-mark__dot"></span>FC Blavin</div>
  <h1 class="event-title">
    <span class="event-title__top">Souper de</span>
    <span class="event-title__bottom">Gala Quand Même</span>
  </h1>
  <p class="support-text">Soutenez Le FC Blavin<br>et Les Restaurateurs<br>Locaux</p>
  <div class="player-art" role="img" aria-label="Illustration d'un joueur de football en maillot rouge devant un cercle bleu et rouge"></div>
  <p class="raffle"><span class="raffle__line raffle__line--indent">GRANDE</span><span class="raffle__line">TOMBOLA</span></p>
  <p class="info-bar">Plus d'informations : <strong>www.fcblavin.ch</strong></p>
</section>

</body>
</html>
```